Design a helpdesk ticketing platform *

We are launching a helpdesk ticketing platform. Very much like quellbox.com, merrylark.com, pivolta.com, brisktray.com etc. We have a full mid-fidelity prototype built and we want someone to build the full fidelity of the product.

You can view the full mid-fidelity prototype here: https://lnk.vexora.net/Qa8Lpw

The best way moving forward is to just design the following 4 pages

- Main Dashboard https://lnk.vexora.net/81hRtd
- All tickets https://lnk.vexora.net/jwNoEb
- Viewing a ticket https://lnk.vexora.net/Ys4VmK
- Contacts https://lnk.vexora.net/pHeXuo

Target Market(s)

Small business owners

Industry/Entity Type

Saas

Number of Pages Required

4 page

Font styles to use
Serif
Sans Serif

Colors

Designer to choose colors to be used in the design.

Requirements
Must have
• Must follow the prototype exactly. We are not looking for any UX changes. We want the designe xactly as the prototype is. We are only looking for design ideas.
Should not have
• modern, clean. We'd love to see the primary color as yellow, purple, orange, green or blue. You choose which one you think looks best and go with that.

```html
<!DOCTYPE html>
<html lang="en">
<head>
<meta charset="utf-8">
<title>HelpHarbor – Unsolved Tickets</title>
<link href="https://fonts.googleapis.com/css2?family=Raleway:wght@400;500;600;700&display=swap" rel="stylesheet">
<style>
:root{
  --ink:#2b2f36;
  --muted:#6b7078;
  --blue:#0aa0ec;
  --green:#7cb82f;
  --red:#f03c2a;
  --orange:#f7931e;
  --line:#e6e8eb;
  --stripe:#f6f7f8;
  --dark:#2d2f33;
  --darker:#252629;
  --footer:#333538;
  --white:#fff;
}
*{box-sizing:border-box;margin:0;padding:0}
html,body{width:854px;height:1200px;overflow:hidden}
body{position:relative;font-family:'Raleway',sans-serif;color:var(--ink);background:var(--white);font-size:8px}
.abs{position:absolute}
.topbar{left:0;top:0;width:854px;height:24px;background:var(--dark);color:#fff;font-size:7px}
.topbar .call{left:78px;top:8px;display:flex;align-items:center;gap:3px}
.topbar .social{right:82px;top:8px;display:flex;gap:13px}
.dot{width:7px;height:7px;border-radius:50%;background:#fff;display:block}
.header{left:0;top:24px;width:854px;height:61px;background:#fff}
.logo{left:75px;top:17px;font-size:23px;font-weight:700;color:#4a4e55;letter-spacing:-.2px}
.nav{left:306px;top:27px;display:flex;gap:0;font-size:7.5px;color:#555a61;letter-spacing:.3px}
.nav span{position:absolute;white-space:nowrap}
.nav .act::after{content:"";position:absolute;left:50%;top:11px;width:5px;height:5px;margin-left:-3px;border-radius:50%;background:var(--orange)}
.band{left:0;top:85px;width:854px;height:43px;background:var(--blue);color:#fff}
.crumb{left:88px;top:16px;font-size:9px;font-weight:500}
.search{left:627px;top:14px;width:141px;height:13px;border-bottom:1px solid rgba(255,255,255,.8);font-size:7.5px}
.stat{top:182px;display:flex;align-items:center;gap:10px}
.stat .ic{width:37px;height:37px;border-radius:50%;display:flex;align-items:center;justify-content:center}
.stat b{display:block;font-size:22px;font-weight:700;line-height:22px}
.stat small{display:block;font-size:9px;color:var(--muted);margin-top:2px}
.vdiv{top:158px;width:1px;height:85px;background:var(--line)}
.sideh{left:78px;top:275px;font-size:11px;font-weight:700}
.deco{height:12px;width:44px}
.side{left:78px;top:318px;width:161px;list-style:none;font-size:7.8px;color:#555a61}
.side li{height:22.5px;display:flex;justify-content:space-between;align-items:flex-start}
.side li.on{color:var(--blue)}
.side .n{width:12px;height:12px;border-radius:50%;background:var(--blue);color:#fff;font-size:6.5px;display:flex;align-items:center;justify-content:center}
.mainh{left:257px;top:275px;font-size:12px;font-weight:700}
.mainsub{left:257px;top:294px;font-size:7.8px;color:var(--muted)}
.btn{left:257px;top:318px;width:119px;height:24px;border-radius:12px;background:var(--blue);color:#fff;font-size:9px;display:flex;align-items:center;justify-content:center;letter-spacing:.2px}
.tickets{left:257px;top:365px;width:517px;border-collapse:collapse;font-size:7.8px;table-layout:fixed;border-top:1px solid var(--line)}
.tickets th{font-weight:500;text-align:left;height:36px;vertical-align:bottom;padding-bottom:6px;border-bottom:2px solid var(--line);color:#444}
.tickets td{vertical-align:top;padding-top:7px;border-bottom:1px solid var(--line);line-height:12px}
.tickets tr.one td{height:24px}
.tickets tr.two td{height:35px}
.tickets tbody tr:nth-child(odd){background:var(--stripe)}
.tickets .subj{color:var(--blue)}
.cb{display:block;width:7px;height:7px;border:1px solid #c5c8cc;margin:2px 0 0 8px;background:#fff}
.tag{display:inline-block;width:31px;height:10px;color:#fff;font-size:5px;font-weight:700;text-align:center;line-height:10px;margin-top:1px}
.high,.private{background:var(--red)}
.low{background:var(--blue)}
.normal,.public{background:var(--green)}
.sstrip{left:0;top:849px;width:854px;height:44px;background:var(--darker)}
.sstrip .dot{position:absolute;top:19px;width:8px;height:8px}
.footer{left:0;top:893px;width:854px;height:270px;background:var(--footer);color:#e4e5e7}
.fcol{top:37px}
.fcol h4{font-size:11.5px;font-weight:700;color:#fff}
.fcol .deco{width:98px;margin:4px 0 8px}
.fcol p{font-size:8.6px;line-height:12.2px;width:160px;color:#d9dadc}
.fcol ul{list-style:none;font-size:8.6px;line-height:13px}
.fcol ul.cats li{height:17.8px}
.fcol ul.arts li{height:31.2px;width:160px}
.email{width:139px;height:21px;border:1px solid #6b6e73;font-size:8px;color:#a8abb0;padding:6px 8px}
.send{left:139px;top:0;width:22px;height:21px;background:var(--blue)}
.copy{left:0;top:1163px;width:854px;height:37px;background:var(--darker);color:#e4e5e7;font-size:9px;text-align:center;line-height:37px}
.support{left:784px;top:1171px;width:63px;height:21px;border-radius:11px;background:var(--blue);color:#fff;font-size:7px;font-weight:700;display:flex;align-items:center;justify-content:center;gap:3px}
</style>
</head>
<body>

<div class="abs topbar">
  <div class="abs call">
    <svg width="7" height="7" viewBox="0 0 10 10"><rect width="10" height="10" rx="2" fill="#fff"/><path d="M3 2.5c0 2.5 2 4.5 4.5 4.5l.5-1.2-1.3-.6-.5.6C5.3 5.4 4.6 4.7 4.2 3.9l.6-.5-.6-1.3z" fill="#2d2f33"/></svg>
    Call our support team: +1 555 0148 220
  </div>
  <div class="abs social"><i class="dot"></i><i class="dot"></i><i class="dot"></i><i class="dot"></i><i class="dot"></i></div>
</div>

<header class="abs header">
  <div class="abs logo">HelpHarbor</div>
  <nav class="abs nav">
    <span style="left:0">HOME ▾</span>
    <span class="act" style="left:51px">TICKET DASH ▾</span>
    <span style="left:131px">KNOWLEDGE BASE ▾</span>
    <span class="act" style="left:236px">FORUM ▾</span>
    <span style="left:296px">CONTACT</span>
    <span style="left:362px">CHANGELOG</span>
    <span style="left:436px"><svg width="9" height="9" viewBox="0 0 10 10"><circle cx="4" cy="4" r="3" fill="none" stroke="#2b2f36" stroke-width="1.5"/><path d="M6.3 6.3L9 9" stroke="#2b2f36" stroke-width="1.6"/></svg></span>
    <span style="left:463px"><svg width="8" height="9" viewBox="0 0 8 10"><path d="M2 4V3a2 2 0 014 0v1" fill="none" stroke="#2b2f36" stroke-width="1.3"/><rect y="4" width="8" height="6" rx="1" fill="#2b2f36"/></svg></span>
  </nav>
</header>

<div class="abs band">
  <div class="abs crumb">Home &nbsp;›&nbsp; Protected: Agent Marlow</div>
  <div class="abs search">Search Knowledgebase...
    <svg class="abs" style="right:2px;top:0" width="8" height="8" viewBox="0 0 10 10"><circle cx="4" cy="4" r="3" fill="none" stroke="#fff" stroke-width="1.6"/><path d="M6.3 6.3L9 9" stroke="#fff" stroke-width="1.8"/></svg>
  </div>
</div>

<div class="abs stat" style="left:78px">
  <div class="ic" style="background:var(--green)"><svg width="20" height="20" viewBox="0 0 20 20"><path d="M4 12l8-8 4 4-8 8z" fill="none" stroke="#fff" stroke-width="1.2"/><path d="M8 10l2 2" stroke="#fff"/></svg></div>
  <div><b style="color:var(--green)">11</b><small>Pending Tickets</small></div>
</div>
<div class="abs vdiv" style="left:310px"></div>
<div class="abs stat" style="left:329px">
  <div class="ic" style="background:var(--blue)"><svg width="20" height="20" viewBox="0 0 20 20"><circle cx="10" cy="10" r="8" fill="none" stroke="#fff" stroke-width="1.2"/><path d="M10 5v5l-3 2" fill="none" stroke="#fff" stroke-width="1.2"/></svg></div>
  <div><b style="color:var(--blue)">74</b><small>Recently Updated</small></div>
</div>
<div class="abs vdiv" style="left:542px"></div>
<div class="abs stat" style="left:561px">
  <div class="ic" style="background:var(--blue)"><svg width="20" height="20" viewBox="0 0 20 20"><rect x="2" y="5" width="16" height="11" rx="1.5" fill="none" stroke="#fff" stroke-width="1.2"/><path d="M2 8h16" stroke="#fff" stroke-width="1.2"/></svg></div>
  <div><b style="color:var(--blue)">73</b><small>New tickets</small></div>
</div>

<div class="abs sideh">DASHBOARD
  <svg class="deco" style="display:block;margin-top:6px" viewBox="0 0 44 12"><path d="M0 6h44" stroke="var(--blue)" stroke-width="1"/><path d="M20 11l4-10" stroke="var(--blue)" stroke-width="1"/></svg>
</div>
<ul class="abs side">
  <li class="on"><span>› All unsolved tickets</span><span class="n">11</span></li>
  <li><span>Your unsolved tickets</span><span class="n">0</span></li>
  <li><span>Unassigned tickets</span><span class="n">57</span></li>
  <li><span>Recently updated tickets</span><span class="n">74</span></li>
  <li><span>New tickets</span><span class="n">73</span></li>
</ul>

<div class="abs mainh">ALL UNSOLVED TICKETS</div>
<div class="abs mainsub">11 unsolved tickets</div>
<div class="abs btn">CHANGE ASSIGNEE</div>

<table class="abs tickets">
  <colgroup><col style="width:23px"><col style="width:209px"><col style="width:86px"><col style="width:58px"><col style="width:46px"><col style="width:51px"><col style="width:44px"></colgroup>
  <thead><tr><th><i class="cb" style="margin-bottom:1px"></i></th><th>Subject</th><th>From</th><th>Posted</th><th>Asignee</th><th>Priority</th><th>Status</th></tr></thead>
  <tbody>
    <tr class="one"><td><i class="cb"></i></td><td class="subj">Не работает Овердрайв</td><td>orin42</td><td>17 day ago</td><td></td><td><span class="tag high">HIGH</span></td><td><span class="tag public">PUBLIC</span></td></tr>
    <tr class="one"><td><i class="cb"></i></td><td class="subj">ererer</td><td>tavelkorin</td><td>18 day ago</td><td>jonwebb</td><td><span class="tag high">HIGH</span></td><td><span class="tag public">PUBLIC</span></td></tr>
    <tr class="two"><td><i class="cb"></i></td><td class="subj">gggg</td><td>Lpvendrak<br>Lpvendrak</td><td>26 day ago</td><td>remi</td><td><span class="tag low">LOW</span></td><td><span class="tag private">PRIVATE</span></td></tr>
    <tr class="two"><td><i class="cb"></i></td><td class="subj">¿Cuanto dinero puedo pedir si tengo un piso que quiero comprar?</td><td>bmorrell</td><td>1 month(s)<br>ago</td><td>remi</td><td><span class="tag normal">NORMAL</span></td><td><span class="tag private">PRIVATE</span></td></tr>
    <tr class="two"><td><i class="cb"></i></td><td class="subj">test</td><td>tullo</td><td>1 month(s)<br>ago</td><td>jonwebb</td><td><span class="tag normal">NORMAL</span></td><td><span class="tag public">PUBLIC</span></td></tr>
    <tr class="two"><td><i class="cb"></i></td><td class="subj">dongle</td><td>Renai Dubrova</td><td>1 month(s)<br>ago</td><td>remi</td><td><span class="tag low">LOW</span></td><td><span class="tag public">PUBLIC</span></td></tr>
    <tr class="two"><td><i class="cb"></i></td><td class="subj">test</td><td>tullo</td><td>1 month(s)<br>ago</td><td>jonwebb</td><td><span class="tag normal">NORMAL</span></td><td><span class="tag public">PUBLIC</span></td></tr>
    <tr class="two"><td><i class="cb"></i></td><td class="subj">dongle</td><td>Renai Dubrova</td><td>1 month(s)<br>ago</td><td>remi</td><td><span class="tag low">LOW</span></td><td><span class="tag public">PUBLIC</span></td></tr>
    <tr class="two"><td><i class="cb"></i></td><td class="subj">test</td><td>kaspen</td><td>1 month(s)<br>ago</td><td>qadev</td><td><span class="tag low">LOW</span></td><td><span class="tag public">PUBLIC</span></td></tr>
    <tr class="one"><td><i class="cb"></i></td><td class="subj">aasd</td><td>Ilko</td><td>3 month ago</td><td>jonwebb</td><td><span class="tag low">LOW</span></td><td><span class="tag public">PUBLIC</span></td></tr>
    <tr class="one"><td><i class="cb"></i></td><td class="subj">Unresolve API Issues</td><td>Odaline Vrask</td><td>3 month ago</td><td></td><td><span class="tag normal">NORMAL</span></td><td><span class="tag private">PRIVATE</span></td></tr>
    <tr class="one"><td><i class="cb"></i></td><td class="subj">Folder</td><td>Teodor Halvik</td><td>3 month ago</td><td>jonwebb</td><td><span class="tag high">HIGH</span></td><td><span class="tag private">PRIVATE</span></td></tr>
    <tr class="one"><td><i class="cb"></i></td><td class="subj">member1 test</td><td>member1</td><td>3 month ago</td><td></td><td><span class="tag normal">NORMAL</span></td><td><span class="tag public">PUBLIC</span></td></tr>
  </tbody>
</table>

<div class="abs sstrip">
  <i class="dot" style="left:199px"></i><i class="dot" style="left:422px"></i><i class="dot" style="left:642px"></i>
</div>

<footer class="abs footer">
  <div class="abs fcol" style="left:78px">
    <h4>ABOUT HELPHARBOR</h4>
    <svg class="deco" viewBox="0 0 98 8"><path d="M0 4h98" stroke="#fff" stroke-width=".8"/><path d="M47 8l3-8" stroke="#fff" stroke-width=".8"/></svg>
    <p>Lorem ipsum dolor sit amet, consectetur adipiscing elit. In erat nulla, suscipit nec nunc sed, cotngue feugiat diam. Suspendisse ultricies, ante eu hendrerit per, ipsum risus egestas leo, et auctor augue justo ut arcu.</p>
  </div>
  <div class="abs fcol" style="left:257px">
    <h4>CATEGORIES</h4>
    <svg class="deco" viewBox="0 0 98 8"><path d="M0 4h98" stroke="#fff" stroke-width=".8"/><path d="M47 8l3-8" stroke="#fff" stroke-width=".8"/></svg>
    <ul class="cats"><li>▭ Blog</li><li>▭ Lorem Ipsum</li><li>▭ Nunc anc erat gravida</li><li>▭ Posts</li><li>▭ Uncategorized</li><li>▭ Vivamus pretium</li></ul>
  </div>
  <div class="abs fcol" style="left:435px">
    <h4>LATEST ARTICLES</h4>
    <svg class="deco" viewBox="0 0 98 8"><path d="M0 4h98" stroke="#fff" stroke-width=".8"/><path d="M47 8l3-8" stroke="#fff" stroke-width=".8"/></svg>
    <ul class="arts">
      <li>▤ What options come with your knowledge base</li>
      <li>▤ Manage your forums in these three simple ways</li>
      <li>▤ How we used ForumKit to develop our ticketing system</li>
      <li>▤ How to best use the Page Composer shortcodes</li>
      <li>▤ 5 best ways to use video knowledgebases</li>
    </ul>
  </div>
  <div class="abs fcol" style="left:614px">
    <h4>NEWSLETTER</h4>
    <svg class="deco" viewBox="0 0 98 8"><path d="M0 4h98" stroke="#fff" stroke-width=".8"/><path d="M47 8l3-8" stroke="#fff" stroke-width=".8"/></svg>
    <div style="position:relative;margin-top:9px">
      <div class="email">Your E-mail:</div>
      <div class="abs send"><svg width="22" height="21" viewBox="0 0 22 21"><path d="M6 11l10-5-3 10-2-4z" fill="#fff"/></svg></div>
    </div>
  </div>
</footer>

<div class="abs copy">Copyright © 2018. HelpHarbor. All rights reserved.</div>
<div class="abs support"><svg width="9" height="9" viewBox="0 0 10 10"><circle cx="5" cy="5" r="4" fill="none" stroke="#fff"/><text x="5" y="7.3" font-size="6" text-anchor="middle" fill="#fff" font-family="Raleway,sans-serif">?</text></svg>Support</div>

</body>
</html>
```